KORBALT

The business want a professional looking business card. We have a scetch we will add but want the extra upgrade, and would like more suggestions for variations of our business cards.

```html
<!DOCTYPE html>
<html lang="en">
<head>
<meta charset="utf-8">
<title>KORBALT – Business Card Options</title>
<link rel="stylesheet" href="https://fonts.googleapis.com/css2?family=Cinzel:wght@400;500&family=Montserrat:wght@300;400;500&display=swap">
<style>
  :root{
    --gold:#b8914a;
    --gold-soft:#d4b57a;
    --cream:#f3ede2;
    --cream-deep:#e8dfcf;
    --ink:#1c1b19;
    --ink-green:#1d2420;
    --header-bg:#3b2d23;
    --header-bg-2:#5a4636;
    --col-1:#e7ddce;
    --col-2:#d8cdbd;
    --col-3:#e3d9cb;
    --text:#4a4038;
    --muted:#7a6e62;
  }
  *{box-sizing:border-box;margin:0;padding:0}
  html,body{width:1200px;height:915px;overflow:hidden;background:#ffffff}
  .board{width:1200px;height:915px;position:relative;font-family:"Montserrat",sans-serif;color:var(--text)}

  /* Header */
  .board-header{height:220px;background:linear-gradient(120deg,var(--header-bg) 0%,var(--header-bg-2) 60%,var(--header-bg) 100%);display:flex;align-items:center;justify-content:center;gap:36px}
  .brand{text-align:center;color:var(--gold-soft)}
  .brand-name{font-family:"Cinzel",serif;font-size:44px;letter-spacing:14px;font-weight:400}
  .brand-since{font-size:11px;letter-spacing:7px;margin-top:6px}
  .header-rule{width:1px;height:70px;background:var(--gold-soft)}
  .tagline{color:var(--cream);font-size:15px;letter-spacing:4px;font-weight:300;line-height:28px}

  /* Columns */
  .options{display:flex;height:695px}
  .option{width:400px;display:flex;flex-direction:column;align-items:center;padding-top:26px}
  .option--soft{background:var(--col-1)}
  .option--bold{background:var(--col-2)}
  .option--modern{background:var(--col-3)}

  .card{width:320px;height:183px;position:relative;overflow:hidden;border-radius:3px;box-shadow:0 6px 14px rgba(40,30,20,.18)}
  .card + .card{margin-top:22px}
  .card--cream{background:var(--cream)}
  .card--black{background:var(--ink)}
  .card--green{background:var(--ink-green)}

  .card-front{display:flex;flex-direction:column;align-items:center;justify-content:center}
  .wordmark{font-family:"Cinzel",serif;color:var(--gold);font-size:28px;letter-spacing:6px;position:relative;z-index:2}
  .wordmark-since{font-size:8px;letter-spacing:4px;color:var(--gold);margin-top:4px;position:relative;z-index:2}
  .gold-frame{position:absolute;inset:12px;border:1px solid var(--gold)}
  .leaf-decor{position:absolute;right:0;bottom:0;width:170px;height:110px;background:radial-gradient(ellipse at 80% 80%,#e6d9c0 0%,rgba(230,217,192,0) 70%)}
  .swoosh{position:absolute;right:0;top:0;width:140px;height:183px;z-index:1}

  .card-back{display:flex;padding:22px 20px}
  .back-info{flex:1}
  .person{font-family:"Cinzel",serif;font-size:12px;letter-spacing:1px;color:var(--gold)}
  .role{font-size:9px;margin-top:3px;color:var(--muted)}
  .card--black .role,.card--green .role{color:#cfc6b8}
  .contact{list-style:none;margin-top:22px}
  .contact li{display:flex;align-items:center;gap:8px;font-size:9px;margin-top:7px;color:var(--text)}
  .card--black .contact li,.card--green .contact li{color:#e2d9ca}
  .contact svg{width:11px;height:11px;flex:none}
  .back-divider{width:1px;background:var(--gold);opacity:.6;margin:0 14px}
  .back-mark{width:96px;display:flex;flex-direction:column;align-items:center;justify-content:center;gap:6px}
  .mark-dot{width:8px;height:8px;border-radius:50%;background:var(--gold)}
  .back-mark .wordmark{font-size:15px;letter-spacing:2px}
  .back-mark .wordmark-since{font-size:6px;letter-spacing:2px;margin-top:0}

  /* Captions */
  .option-icon{margin-top:30px;width:26px;height:26px}
  .option-title{margin-top:12px;font-size:13px;letter-spacing:5px;color:var(--text)}
  .option-style{margin-top:18px;font-size:11px;letter-spacing:3px;color:var(--text)}
  .option-desc{margin-top:18px;font-size:11px;line-height:19px;text-align:center;color:var(--text);width:240px}
</style>
</head>
<body>
<main class="board">
  <header class="board-header">
    <div class="brand">
      <div class="brand-name">KORBALT</div>
      <div class="brand-since">SINCE 2026</div>
    </div>
    <div class="header-rule"></div>
    <p class="tagline">Crafting Tomorrow,<br>Together</p>
  </header>

  <section class="options">
    <!-- Option 1 -->
    <article class="option option--soft">
      <div class="card card--cream card-front">
        <div class="leaf-decor" role="img" aria-label="Faint organic leaf line pattern"></div>
        <div class="wordmark">KORBALT</div>
        <div class="wordmark-since">SINCE 2026</div>
      </div>
      <div class="card card--cream card-back">
        <div class="back-info">
          <div class="person">ERIK HALVORSEN</div>
          <div class="role">CEO &amp; Founder</div>
          <ul class="contact">
            <li><svg viewBox="0 0 12 12" fill="none" stroke="#b8914a"><rect x="3.5" y="1" width="5" height="10" rx="1"/></svg>0047 40012345</li>
            <li><svg viewBox="0 0 12 12" fill="none" stroke="#b8914a"><rect x="1" y="2.5" width="10" height="7"/><path d="M1 2.5l5 4 5-4"/></svg>hello@korbalt.example</li>
            <li><svg viewBox="0 0 12 12" fill="none" stroke="#b8914a"><circle cx="6" cy="6" r="5"/><path d="M1 6h10M6 1c2.5 3 2.5 7 0 10M6 1c-2.5 3-2.5 7 0 10"/></svg>www.korbalt.example</li>
          </ul>
        </div>
        <div class="back-divider"></div>
        <div class="back-mark">
          <span class="mark-dot"></span>
          <div class="wordmark">KORBALT</div>
          <div class="wordmark-since">SINCE 2026</div>
        </div>
      </div>
      <svg class="option-icon" viewBox="0 0 26 26" fill="none" stroke="#4a4038" stroke-width="1"><path d="M5 21C5 11 11 5 21 5c0 10-6 16-16 16z"/><path d="M5 21L15 11"/></svg>
      <div class="option-title">OPTION 1</div>
      <div class="option-style">SOFT &amp; NATURAL</div>
      <p class="option-desc">Clean, warm and timeless with subtle organic elements.</p>
    </article>

    <!-- Option 2 -->
    <article class="option option--bold">
      <div class="card card--black card-front">
        <div class="gold-frame"></div>
        <div class="wordmark">KORBALT</div>
        <div class="wordmark-since">SINCE 2026</div>
      </div>
      <div class="card card--black card-back">
        <div class="back-info">
          <div class="person">ERIK HALVORSEN</div>
          <div class="role">CEO &amp; Founder</div>
          <ul class="contact">
            <li><svg viewBox="0 0 12 12" fill="none" stroke="#b8914a"><rect x="3.5" y="1" width="5" height="10" rx="1"/></svg>0047 40012345</li>
            <li><svg viewBox="0 0 12 12" fill="none" stroke="#b8914a"><rect x="1" y="2.5" width="10" height="7"/><path d="M1 2.5l5 4 5-4"/></svg>hello@korbalt.example</li>
            <li><svg viewBox="0 0 12 12" fill="none" stroke="#b8914a"><circle cx="6" cy="6" r="5"/><path d="M1 6h10M6 1c2.5 3 2.5 7 0 10M6 1c-2.5 3-2.5 7 0 10"/></svg>www.korbalt.example</li>
          </ul>
        </div>
        <div class="back-divider"></div>
        <div class="back-mark">
          <span class="mark-dot"></span>
          <div class="wordmark">KORBALT</div>
          <div class="wordmark-since">SINCE 2026</div>
        </div>
      </div>
      <svg class="option-icon" viewBox="0 0 26 26" fill="none" stroke="#4a4038" stroke-width="1"><path d="M3 9l4-5h12l4 5-10 13z"/><path d="M3 9h20M9 9l4 13 4-13M7 4l2 5 4-5 4 5 2-5"/></svg>
      <div class="option-title">OPTION 2</div>
      <div class="option-style">BOLD &amp; LUXURY</div>
      <p class="option-desc">Rich black with gold foil for a premium and confident impression.</p>
    </article>

    <!-- Option 3 -->
    <article class="option option--modern">
      <div class="card card--cream card-front">
        <svg class="swoosh" viewBox="0 0 140 183" preserveAspectRatio="none">
          <path d="M140 0 C95 40 60 110 20 183 L140 183 Z" fill="#c9a561"/>
          <path d="M140 30 C110 80 90 130 70 183 L140 183 Z" fill="#2a2b28"/>
        </svg>
        <div class="wordmark">KORBALT</div>
        <div class="wordmark-since">SINCE 2026</div>
      </div>
      <div class="card card--green card-back">
        <div class="back-info">
          <div class="person">ERIK HALVORSEN</div>
          <div class="role">CEO &amp; Founder</div>
          <ul class="contact">
            <li><svg viewBox="0 0 12 12" fill="none" stroke="#b8914a"><rect x="3.5" y="1" width="5" height="10" rx="1"/></svg>0047 40012345</li>
            <li><svg viewBox="0 0 12 12" fill="none" stroke="#b8914a"><rect x="1" y="2.5" width="10" height="7"/><path d="M1 2.5l5 4 5-4"/></svg>hello@korbalt.example</li>
            <li><svg viewBox="0 0 12 12" fill="none" stroke="#b8914a"><circle cx="6" cy="6" r="5"/><path d="M1 6h10M6 1c2.5 3 2.5 7 0 10M6 1c-2.5 3-2.5 7 0 10"/></svg>www.korbalt.example</li>
          </ul>
        </div>
        <div class="back-divider"></div>
        <div class="back-mark">
          <span class="mark-dot"></span>
          <div class="wordmark">KORBALT</div>
          <div class="wordmark-since">SINCE 2026</div>
        </div>
      </div>
      <svg class="option-icon" viewBox="0 0 26 26" fill="none" stroke="#4a4038" stroke-width="1"><path d="M3 9l4-5h12l4 5-10 13z"/><path d="M3 9h20M9 9l4 13 4-13"/></svg>
      <div class="option-title">OPTION 3</div>
      <div class="option-style">MODERN &amp; MINIMAL</div>
      <p class="option-desc">Clean lines, refined colors and a fresh, contemporary feel.</p>
    </article>
  </section>
</main>
</body>
</html>
```